business card design for luxurious real estate brand

using the attached logo, i am looking for a 2-sided business card design. the back should be the gold logo on black background. the front needs to include: gold logo, name, phone, email, and website

Industry/Entity Type

real estate

Contact Information for Business Card

logo, name, email, phone, website

Font styles to use
Sans Serif

```html
<!DOCTYPE html>
<html lang="en">
<head>
<meta charset="UTF-8">
<title>Casa Brightwater — Business Card</title>
<link href="https://fonts.googleapis.com/css2?family=Josefin+Sans:wght@600&family=Source+Sans+3:wght@400;700&display=swap" rel="stylesheet">
<style>
  :root {
    --bg: #e4e4e4;
    --card-dark: #2b2a29;
    --card-light: #f4f4f4;
    --gold: #c9a228;
    --gold-bright: #f0c11a;
    --ink: #2a2a2a;
  }
  * { margin: 0; padding: 0; box-sizing: border-box; }
  html, body { width: 1200px; height: 960px; overflow: hidden; }
  body {
    background: var(--bg);
    position: relative;
    font-family: "Source Sans 3", sans-serif;
  }
  .card {
    position: absolute;
    width: 612px;
    height: 350px;
  }
  .card-back {
    left: 293px; top: 118px;
    background: var(--card-dark);
  }
  .card-front {
    left: 295px; top: 506px;
    background: var(--card-light);
  }
  .brand-name {
    font-family: "Josefin Sans", sans-serif;
    font-weight: 600;
    color: var(--gold);
    letter-spacing: 0.14em;
    text-transform: uppercase;
    white-space: nowrap;
  }
  .card-back .brand {
    position: absolute;
    left: 0; right: 0; top: 150px;
    display: flex; flex-direction: column; align-items: center; gap: 22px;
  }
  .brand-square {
    width: 22px; height: 22px; background: var(--gold);
  }
  .card-back .brand-name { font-size: 27px; }
  .card-front .brand {
    position: absolute;
    left: 43px; top: 112px;
  }
  .card-front .brand-name { font-size: 20px; }
  .holder {
    position: absolute;
    left: 43px; top: 262px;
  }
  .holder-name {
    font-weight: 700;
    font-size: 19px;
    color: var(--gold-bright);
    letter-spacing: 0.01em;
    line-height: 24px;
  }
  .holder-title {
    font-size: 15px;
    color: var(--ink);
    line-height: 22px;
  }
  .contacts {
    position: absolute;
    left: 355px; top: 244px;
    list-style: none;
  }
  .contacts li {
    display: flex; align-items: center; gap: 6px;
    font-size: 15px; color: var(--ink);
    line-height: 21px;
  }
  .contacts svg { width: 14px; height: 14px; flex: none; }
</style>
</head>
<body>
  <section class="card card-back">
    <div class="brand">
      <span class="brand-square"></span>
      <span class="brand-name">Casa Brightwater</span>
    </div>
  </section>

  <section class="card card-front">
    <div class="brand">
      <span class="brand-name">Casa Brightwater</span>
    </div>
    <div class="holder">
      <p class="holder-name">DANIEL WHITFORD</p>
      <p class="holder-title">Managing Director</p>
    </div>
    <ul class="contacts">
      <li>
        <svg viewBox="0 0 24 24" fill="none" stroke="#f0c11a" stroke-width="2.4" stroke-linecap="round" stroke-linejoin="round"><path d="M21 16.5v3a2 2 0 0 1-2.2 2A19 19 0 0 1 2.5 5.2 2 2 0 0 1 4.5 3h3a2 2 0 0 1 2 1.7l.5 2.8a2 2 0 0 1-.6 1.8L8 10.6a16 16 0 0 0 5.4 5.4l1.3-1.4a2 2 0 0 1 1.8-.6l2.8.5a2 2 0 0 1 1.7 2z"/></svg>
        (555) 014-2380
      </li>
      <li>
        <svg viewBox="0 0 24 24" fill="none" stroke="#f0c11a" stroke-width="2.4" stroke-linejoin="round"><rect x="2" y="5" width="20" height="14"/><path d="M2 5l10 8 10-8"/></svg>
        daniel@casabrightwater.com
      </li>
      <li>
        <svg viewBox="0 0 24 24" fill="none" stroke="#f0c11a" stroke-width="2.2"><circle cx="12" cy="12" r="10"/><path d="M2 12h20M12 2c3 3 4 6.5 4 10s-1 7-4 10c-3-3-4-6.5-4-10s1-7 4-10z"/></svg>
        www.casabrightwater.com
      </li>
    </ul>
  </section>
</body>
</html>
```